Sticker proposal and a brand name for matured cheese slices

We need a full face sticker design and a brand name for a packaging of cheese slices. The cheese is mature holland gouda (aged for 2-3 months) and lactose free which we want to be addressed. Dimensions of the sticker should be 140x115mm. We want to make up a name for the packages like brovintel did, but not based on the origin of the cheese. The market we are going to sell at first is the greek one. Our Company is VELMIRA SA and website, velmira-sa.com. The sticker style should be modern, referring to nature, tradition or technology and bright coloured.

Reason: we need more designs to choose from

Target Market(s)

supermarkets

Industry/Entity Type

Food Store

Requirements
Must have
• lactose free, mature, slices
Nice to have
• blue, green colours. a transparent hole so that the cheese slice can be seen. toast/sandwich figure as it is mostly used for sandwich
Should not have
• dark colours

```html
<!DOCTYPE html>
<html lang="en">
<head>
<meta charset="utf-8">
<title>Arvelo Matured Cheese Slices – Sticker</title>
<link rel="stylesheet" href="https://fonts.googleapis.com/css2?family=Comfortaa:wght@600;700&family=Oswald:wght@400&family=Nunito:wght@700;800&display=swap">
<style>
  :root {
    --page: #ffffff;
    --cream: #f8ecb4;
    --cream-light: #fcf4cf;
    --sky-top: #3d8fd6;
    --sky-low: #bfe0f2;
    --field: #c9b33f;
    --field-green: #9eb33a;
    --royal: #1a55a8;
    --brand-disc: #3a73c4;
    --navy: #1b3f86;
    --cyan: #2aa6e0;
    --ribbon: #3e86cf;
    --ribbon-dark: #24579e;
    --band: #f2b21c;
    --grass-dark: #2f8d19;
    --grass-light: #8fd13a;
    --cheese: #f1dc86;
    --border: #4a4a4a;
    --white: #ffffff;
  }
  html, body {
    margin: 0;
    width: 831px;
    height: 1200px;
    overflow: hidden;
    background: var(--page);
  }
  .sticker {
    position: absolute;
    left: 35px;
    top: 137px;
    width: 760px;
    height: 926px;
  }
  .sticker svg { display: block; }
  .brand-name { font-family: "Nunito", sans-serif; font-weight: 700; font-size: 58px; fill: var(--white); }
  .ribbon-text { font-family: "Comfortaa", sans-serif; font-weight: 700; font-size: 50px; fill: var(--white); }
  .natural-text { font-family: "Nunito", sans-serif; font-weight: 800; font-size: 34px; fill: var(--white); }
  .cheese-word { font-family: "Comfortaa", sans-serif; font-weight: 600; font-size: 84px; fill: var(--cyan); }
  .slices-word { font-family: "Comfortaa", sans-serif; font-weight: 700; font-size: 150px; fill: var(--royal); }
  .matured-word { font-family: "Oswald", sans-serif; font-weight: 400; font-size: 70px; fill: var(--navy); }
  .net-weight { font-family: "Nunito", sans-serif; font-weight: 700; font-size: 27px; fill: var(--navy); }
</style>
</head>
<body>
<div class="sticker">
  <svg width="760" height="926" viewBox="0 0 760 926" xmlns="http://www.w3.org/2000/svg">
    <defs>
      <clipPath id="sticker-shape"><rect x="2" y="2" width="756" height="922" rx="34"/></clipPath>
      <linearGradient id="scene-fill" x1="0" y1="0" x2="0" y2="1">
        <stop offset="0" stop-color="var(--sky-top)"/>
        <stop offset="0.45" stop-color="var(--sky-low)"/>
        <stop offset="0.62" stop-color="var(--field)"/>
        <stop offset="1" stop-color="var(--field-green)"/>
      </linearGradient>
      <linearGradient id="cream-fill" x1="0" y1="0" x2="0" y2="1">
        <stop offset="0" stop-color="var(--cream-light)"/>
        <stop offset="1" stop-color="var(--cream)"/>
      </linearGradient>
      <radialGradient id="cheese-fill" cx="0.6" cy="0.45" r="0.6">
        <stop offset="0" stop-color="var(--cheese)"/>
        <stop offset="1" stop-color="var(--cream)" stop-opacity="0"/>
      </radialGradient>
      <linearGradient id="grass-fill" x1="0" y1="0" x2="0" y2="1">
        <stop offset="0" stop-color="var(--grass-light)" stop-opacity="0"/>
        <stop offset="0.35" stop-color="var(--grass-light)"/>
        <stop offset="1" stop-color="var(--grass-dark)"/>
      </linearGradient>
    </defs>

    <g clip-path="url(#sticker-shape)">
      <rect class="sticker-base" width="760" height="926" fill="url(#cream-fill)"/>

      <rect class="pasture-scene" x="0" y="0" width="760" height="284" fill="url(#scene-fill)"
            role="img" aria-label="Illustrated countryside with sky, clouds, fields and grazing cows"/>

      <rect class="cheese-photo" x="30" y="340" width="700" height="370" fill="url(#cheese-fill)"
            role="img" aria-label="Photo of a block of cheese with thin slices"/>

      <rect class="grass-strip" x="0" y="640" width="760" height="286" fill="url(#grass-fill)"
            role="img" aria-label="Illustrated green grass along the bottom edge"/>

      <polygon class="natural-corner" points="534,0 760,0 760,160" fill="var(--royal)"/>
      <text class="natural-text" text-anchor="middle" transform="translate(666,48) rotate(36)">
        <tspan x="0" y="0">100%</tspan><tspan x="-6" y="34">Natural</tspan>
      </text>

      <rect class="grade-band" x="0" y="746" width="760" height="80" fill="var(--band)"/>
    </g>

    <rect class="sticker-outline" x="2" y="2" width="756" height="922" rx="34" fill="none" stroke="var(--border)" stroke-width="3"/>

    <circle class="brand-disc" cx="385" cy="180" r="144" fill="var(--brand-disc)"/>
    <text class="brand-name" x="385" y="190" text-anchor="middle">Arvelo</text>

    <g class="lactose-ribbon">
      <path d="M200 262 Q390 296 580 262 L590 312 Q390 350 196 312 Z" fill="var(--ribbon)"/>
      <path d="M196 312 L230 330 L226 306 Z" fill="var(--ribbon-dark)"/>
      <path d="M590 312 L556 332 L560 306 Z" fill="var(--ribbon-dark)"/>
      <text class="ribbon-text" x="390" y="314" text-anchor="middle">lactose free</text>
    </g>

    <text class="cheese-word" x="286" y="494">Cheese</text>
    <text class="slices-word" x="130" y="590">Slices</text>

    <circle class="cert-badge" cx="84" cy="783" r="27" fill="var(--white)" stroke="var(--grass-dark)" stroke-width="4"/>
    <text class="matured-word" x="408" y="810" text-anchor="middle">MATURED</text>
    <text class="net-weight" x="688" y="778" text-anchor="middle">
      <tspan x="688" dy="0">Net</tspan><tspan x="688" dy="26">weight</tspan>
    </text>
  </svg>
</div>
</body>
</html>
```